Slider needed for Database Documentation Topic

We need a slider to promote a content area of a web site. I'm listing this as a poster because the posters I have seen on Quillbarn portfolios most closely resemble the combination or art and text I am looking for.
The content area we are promoting with this graphic will clarify the design and use of a complicated database. The title of the content area is "The Marbled QZ Database" and the banner should use that title.
To 'illuminate' something means to cast light on it, and this content area will help shed light on a complicated thing – the content will use diagrams, text, and examples to clarify the database. Another meaning is that an illuminated manuscript is a manuscript brought to life with pictures, and in a way that is also what this content area will do.
One idea for the slider might be a light bulb, lamp, candle or flashlight lighting up the words "QZ Database". Another idea would be the type of illustration you see if you search for "Illuminated manuscript"
But I'm not committed to any particular idea - in the past I have been pleased to see ideas that are different than my own but accomplish the same thing, so please feel free to use your judgement or ask any questions.
In addition to the title (The Marbled QZ Database) the graphic should allow room for three smaller lines of text – the three bullet items below:
- Guide to understanding the QZ database
- Data sources, uses and relationships explained with illustrations
- New content! Customers
The last bullet item will change as the content is added.
Some particulars ...
SIZE - 600 high x 1200 wide pixels
PHOTOS vs ILLUSTRATION - I am open to either one.

```html
<!DOCTYPE html>
<html lang="en">
<head>
<meta charset="utf-8">
<title>The Marbled QZ Database</title>
<link rel="stylesheet" href="https://fonts.googleapis.com/css2?family=Questrial&family=Poppins:wght@300&family=Montserrat:wght@600&display=swap">
<style>
  :root {
    --page: #ffffff;
    --ink-dark: #1a0b04;
    --ember: #4a1f06;
    --night: #000000;
    --title-red: #e8401a;
    --title-white: #ffffff;
    --bullet-red: #e8401a;
    --copy: #f4ece6;
    --glow-gold: #ffd21c;
    --glow-amber: #ff9a1a;
    --glow-orange: #f2531a;
    --glint: #fff4d8;
  }
  * { margin: 0; padding: 0; box-sizing: border-box; }
  html, body {
    width: 1200px;
    height: 686px;
    overflow: hidden;
    background: var(--page);
  }
  .slider {
    position: absolute;
    left: 82px;
    top: 84px;
    width: 1035px;
    height: 518px;
    overflow: hidden;
    background: var(--night);
    box-shadow: 4px 6px 10px rgba(0, 0, 0, 0.35);
  }
  .slider__backdrop {
    position: absolute;
    inset: 0;
    background: linear-gradient(100deg, var(--ember) 0%, #3a1805 40%, #1f0c03 78%, var(--night) 91%);
  }
  .slider__art {
    position: absolute;
    inset: 0;
    width: 1035px;
    height: 518px;
  }
  .slider__title {
    position: absolute;
    left: 30px;
    top: 56px;
    line-height: 1;
    font-weight: normal;
  }
  .title__lead {
    display: block;
    margin-left: 58px;
    font-family: "Poppins", sans-serif;
    font-weight: 300;
    font-size: 48px;
    color: var(--title-red);
    letter-spacing: -1.5px;
  }
  .title__main {
    display: block;
    margin-top: 2px;
    font-family: "Montserrat", sans-serif;
    font-weight: 600;
    font-size: 71px;
    color: var(--title-white);
    letter-spacing: -1.5px;
  }
  .slider__points {
    position: absolute;
    left: 122px;
    top: 197px;
    width: 360px;
    list-style: none;
    font-family: "Questrial", sans-serif;
    font-size: 16.5px;
    line-height: 17px;
    color: var(--copy);
  }
  .slider__points li {
    position: relative;
    padding-left: 16px;
    margin-bottom: 7px;
  }
  .slider__points li::before {
    content: "";
    position: absolute;
    left: 0;
    top: 5px;
    width: 6px;
    height: 6px;
    border-radius: 50%;
    background: var(--bullet-red);
  }
</style>
</head>
<body>
  <section class="slider">
    <div class="slider__backdrop"></div>
    <svg class="slider__art" viewBox="0 0 1035 518" role="img" aria-label="Sweeping swirl of glowing gold and orange stars curving up from the lower left across the dark banner, scattered with small points of light, and a bright sparkle of light beside the title">
      <defs>
        <filter id="soft" x="-20%" y="-20%" width="140%" height="140%"><feGaussianBlur stdDeviation="9"/></filter>
        <filter id="haze" x="-30%" y="-30%" width="160%" height="160%"><feGaussianBlur stdDeviation="22"/></filter>
        <radialGradient id="glint-halo">
          <stop offset="0" stop-color="#fff6dc" stop-opacity="1"/>
          <stop offset="0.15" stop-color="#ffc46a" stop-opacity="0.8"/>
          <stop offset="1" stop-color="#ff8a20" stop-opacity="0"/>
        </radialGradient>
        <radialGradient id="ember-glow">
          <stop offset="0" stop-color="#ffb040" stop-opacity="0.55"/>
          <stop offset="1" stop-color="#ff7010" stop-opacity="0"/>
        </radialGradient>
      </defs>
      <!-- broad haze under the swirl -->
      <g filter="url(#haze)" opacity="0.45">
        <path d="M0 300 C150 330 300 420 330 518" fill="none" stroke="var(--glow-amber)" stroke-width="90"/>
        <path d="M360 340 C430 230 520 120 620 0" fill="none" stroke="var(--glow-orange)" stroke-width="90"/>
      </g>
      <!-- swirl bands -->
      <g filter="url(#soft)" fill="none" stroke-linecap="round">
        <path d="M0 230 C40 300 80 380 120 518" stroke="var(--glow-gold)" stroke-width="22" opacity="0.75"/>
        <path d="M60 320 C150 360 220 430 250 518" stroke="var(--glow-gold)" stroke-width="20" opacity="0.7"/>
        <path d="M120 360 C230 370 300 430 340 518" stroke="var(--glow-amber)" stroke-width="20" opacity="0.7"/>
        <path d="M300 380 C380 330 420 400 430 518" stroke="var(--glow-orange)" stroke-width="18" opacity="0.7"/>
        <path d="M400 350 C470 260 520 200 560 0" stroke="var(--glow-orange)" stroke-width="20" opacity="0.75"/>
        <path d="M460 370 C560 300 600 200 700 0" stroke="var(--glow-orange)" stroke-width="18" opacity="0.7"/>
        <path d="M540 400 C620 330 700 220 760 0" stroke="var(--glow-orange)" stroke-width="16" opacity="0.6"/>
        <path d="M560 40 C640 40 700 60 790 90" stroke="var(--glow-orange)" stroke-width="16" opacity="0.6"/>
        <path d="M560 100 C640 110 720 140 790 170" stroke="var(--glow-orange)" stroke-width="14" opacity="0.55"/>
      </g>
      <!-- scattered points of light -->
      <g fill="url(#ember-glow)">
        <circle cx="885" cy="22" r="22"/><circle cx="810" cy="205" r="24"/>
        <circle cx="760" cy="280" r="20"/><circle cx="865" cy="350" r="22"/>
        <circle cx="915" cy="380" r="20"/><circle cx="540" cy="510" r="22"/>
        <circle cx="18" cy="230" r="26"/><circle cx="120" cy="490" r="26"/>
        <circle cx="270" cy="490" r="28"/><circle cx="980" cy="60" r="12"/>
        <circle cx="700" cy="450" r="18"/><circle cx="930" cy="230" r="16"/>
      </g>
      <!-- sparkle beside the title -->
      <circle cx="515" cy="108" r="46" fill="url(#glint-halo)"/>
      <g stroke="var(--glint)" stroke-linecap="round">
        <line x1="515" y1="26" x2="515" y2="190" stroke-width="2" opacity="0.85"/>
        <line x1="435" y1="108" x2="600" y2="108" stroke-width="2" opacity="0.85"/>
        <line x1="488" y1="81" x2="542" y2="135" stroke-width="1.2" opacity="0.6"/>
        <line x1="542" y1="81" x2="488" y2="135" stroke-width="1.2" opacity="0.6"/>
      </g>
      <circle cx="515" cy="108" r="5" fill="#ffffff"/>
      <!-- dark edge on the right -->
      <rect x="946" y="0" width="89" height="518" fill="var(--night)" opacity="0.85"/>
    </svg>
    <h1 class="slider__title">
      <span class="title__lead">The Marbled</span>
      <span class="title__main">QZ Database</span>
    </h1>
    <ul class="slider__points">
      <li>Guide to understanding the QZ database</li>
      <li>Data sources, uses and relationships explained with illustrations</li>
      <li>New content! Customers</li>
    </ul>
  </section>
</body>
</html>
```